Tallwood Ridge firewood

It a new firewood outlet in Jindabyne nsw that will only sell top hardwood firewood (ironbark , red gum, grey gum, an box mix. I would like to see a web page the we can do order online payment for delivery. It will all so need to have photos of the firewood. I all so have logo for tallwood ridge firewood
Must have a modem look but easy to use I would like to see a black back ground of some sort.

Here are some other firewood web pages for ideas and firewood info
http://www.kestrelburnfuel.com.au
http://www.brindlefirewood.com.au
http://www.coppertonfirewood.com.au
http://www.wattleyhearthlogs.com.au/firewood

```html
<!DOCTYPE html>
<html lang="en">
<head>
<meta charset="utf-8">
<title>Tallwood Ridge firewood</title>
<link href="https://fonts.googleapis.com/css2?family=Open+Sans:wght@400;600&family=Roboto+Condensed:wght@400&family=Ubuntu:wght@300;400;500;700&display=swap" rel="stylesheet">
<style>
:root{
  --bg:#000;
  --header-top:#2a2a2a;
  --nav:#3a3a3a;
  --nav-line:#232323;
  --white:#fff;
  --grey:#a9a9a9;
  --light:#dcdcdc;
  --blue:#3a9be0;
  --blue-dark:#1a6fc4;
  --gold:#f0b429;
  --yellow:#f7c51e;
  --footer:#333;
  --wood-a:#c98c52;
  --wood-b:#8a5a30;
  --wood-c:#e8b27a;
}
*{margin:0;padding:0;box-sizing:border-box}
html,body{width:969px;height:1200px;overflow:hidden;background:var(--bg)}
body{position:relative;font-family:"Open Sans",sans-serif;color:var(--white)}
.abs{position:absolute}

.site-header{left:0;top:0;width:969px;height:159px;background:linear-gradient(180deg,var(--header-top) 0%,#0d0d0d 60%,#000 100%)}
.brand{left:385px;top:8px;width:200px;text-align:center}
.brand-mark{width:112px;height:104px;margin:0 auto;border-radius:50%;border:4px solid var(--white);background:#111}
.brand-name{margin-top:4px;font-family:"Ubuntu",sans-serif;font-weight:700;font-size:16px;color:var(--blue);letter-spacing:.2px}
.call{right:68px;top:96px;text-align:right;font-family:"Ubuntu",sans-serif}
.call-label{font-size:16px;color:#d0d0d0}
.call-number{font-size:25px;color:var(--gold);font-weight:500;line-height:1.15}

.main-nav{left:0;top:159px;width:969px;height:46px;background:var(--nav);border-top:1px solid #555;border-bottom:1px solid #222}
.main-nav ul{list-style:none;position:absolute;left:59px;top:0;display:flex;height:45px}
.main-nav li{font-family:"Roboto Condensed",sans-serif;font-size:15px;color:var(--white);display:flex;align-items:center;justify-content:center;border-left:1px solid var(--nav-line)}
.main-nav li:first-child{border-left:none}

.hero{left:0;top:205px;width:969px;height:348px;background:radial-gradient(circle at 20% 30%,var(--wood-c),transparent 40%),radial-gradient(circle at 75% 80%,var(--wood-c),transparent 35%),linear-gradient(135deg,var(--wood-a),var(--wood-b) 50%,var(--wood-a))}
.hero-title{left:60px;top:88px;font-family:"Open Sans",sans-serif;font-weight:600;text-shadow:0 1px 3px rgba(0,0,0,.5)}
.hero-title .line1{font-size:29px;line-height:36px}
.hero-title .line2{font-size:38px;line-height:46px;font-weight:600}
.hero-text{left:60px;top:171px;width:380px;font-size:11px;line-height:17px;font-weight:600}
.hero-dots{left:60px;top:220px;display:flex;gap:3px}
.hero-dots span{width:12px;height:12px;border-radius:50%;background:var(--white)}
.hero-photo{left:516px;top:35px;width:392px;height:266px;border:7px solid var(--white);transform:rotate(-2deg);box-shadow:0 4px 10px rgba(0,0,0,.5);background:radial-gradient(ellipse at 50% 60%,#ff6a1a 0%,#9a2a08 30%,#1b1b1b 60%),linear-gradient(180deg,#8c8c8c 0%,#333 40%,#1a1a1a 100%)}

.welcome h1{left:57px;top:585px;font-family:"Ubuntu",sans-serif;font-weight:300;font-size:28px}
.welcome p{left:59px;top:624px;width:550px;font-size:11.2px;line-height:21px;color:var(--light)}

.segment h2{font-family:"Ubuntu",sans-serif;font-weight:500;font-size:19.5px;color:var(--blue)}
.segment h3{font-weight:400;font-size:12.7px;margin-top:4px}
.segment p{font-size:11px;line-height:21px;color:var(--grey);margin-top:3px;width:260px}
.seg-res{left:60px;top:757px}
.seg-com{left:351px;top:757px}

.why h2{left:59px;top:909px;font-family:"Ubuntu",sans-serif;font-weight:300;font-size:19.5px}
.why-photo{left:60px;top:945px;width:129px;height:103px;border:1px solid #555;background:radial-gradient(ellipse at 50% 55%,#ffc23a 0%,#ff6a00 30%,#7a1d04 60%,#1a0600 100%)}
.why p{left:199px;top:942px;width:410px;font-size:11px;line-height:21px;color:var(--grey)}

.order-box{left:647px;top:582px;width:258px;height:265px;border:1px solid #555;border-radius:8px;background:#0b0b0b;overflow:hidden}
.order-head{height:40px;background:linear-gradient(180deg,#4aa8f0,var(--blue-dark));font-family:"Ubuntu",sans-serif;font-size:18.5px;padding:10px 0 0 21px}
.order-photo{position:absolute;left:17px;top:52px;width:226px;height:94px;background:linear-gradient(90deg,#c9d3dc,#eef2f5 50%,#b8c3cc)}
.order-title{position:absolute;left:19px;top:155px;font-size:12.5px}
.order-text{position:absolute;left:19px;top:173px;width:225px;font-size:10.5px;line-height:19px;color:var(--grey)}
.order-btn{position:absolute;left:19px;top:217px;width:101px;height:29px;border-radius:3px;background:var(--yellow);color:#1a1a1a;font-size:11px;font-weight:600;display:flex;align-items:center;justify-content:center}

.offers h2{left:654px;top:867px;font-family:"Ubuntu",sans-serif;font-weight:400;font-size:22px;color:var(--blue)}
.offers h3{left:656px;top:900px;font-family:"Ubuntu",sans-serif;font-weight:400;font-size:13.5px}
.offers p{left:656px;width:245px;font-family:"Ubuntu",sans-serif;font-weight:300;font-size:11px;line-height:18.4px;color:var(--light)}
.offers .p1{top:923px}
.offers .p2{top:1019px}

.site-footer{left:0;top:1088px;width:969px;height:112px;background:var(--footer)}
.foot-links{left:55px;top:28px;font-family:"Roboto Condensed",sans-serif;font-size:12px;color:var(--white)}
.foot-links span{margin:0 4px}
.copyright{left:55px;top:53px;font-family:"Ubuntu",sans-serif;font-weight:300;font-size:11px;color:#ccc}
.social{left:814px;top:30px;display:flex;gap:7px}
.social span{width:19px;height:19px;border-radius:2px}
.cards{left:777px;top:62px;display:flex;gap:5px}
.cards span{width:31px;height:20px;border-radius:2px;background:#e8e8e8}
</style>
</head>
<body>

<header class="site-header abs">
  <div class="brand abs">
    <div class="brand-mark" role="img" aria-label="Firewood company emblem"></div>
    <div class="brand-name">Tallwood Ridge firewood</div>
  </div>
  <div class="call abs">
    <div class="call-label">CALL US NOW</div>
    <div class="call-number">0400 555 218</div>
  </div>
</header>

<nav class="main-nav abs">
  <ul>
    <li style="width:75px">HOME</li>
    <li style="width:97px">ABOUT US</li>
    <li style="width:107px">FIRE WQOD</li>
    <li style="width:71px">PRICE</li>
    <li style="width:93px">DELIVERY</li>
    <li style="width:113px">ACCESORIES</li>
    <li style="width:113px">ORDER NOW</li>
    <li style="width:93px">SUPPORT</li>
    <li style="width:97px">CONTACT</li>
  </ul>
</nav>

<section class="hero abs" role="img" aria-label="Stacked hardwood firewood logs">
  <div class="hero-title abs">
    <div class="line1">Mauris vel lacus vitae felis</div>
    <div class="line2">Phasellus dolor sceleris</div>
  </div>
  <p class="hero-text abs">Aliquam nec erat at purus cursus interdum Vestibulum ligula augue bibendum accumsan vestibulum ut commodo a mi</p>
  <div class="hero-dots abs"><span></span><span></span><span></span><span></span></div>
  <div class="hero-photo abs" role="img" aria-label="Wood fire burning in a fireplace"></div>
</section>

<section class="welcome">
  <h1 class="abs">Welcome to Our Website Mainpage..</h1>
  <p class="abs">Etiam eu urna Sed porta Suspendisse quam leo molestie sed luctus quis feugiat in pede Fusce tellus Sed metus augue convallis et vehicula ut pulvinar eu ante Integer orci tellus tristique vitae consequat nec porta vel lectus Nulla sit amet diam Duis non nunclibero a tempus libero lectus feugiat felis Morbi diam mauris viverra in gravida eu mattis in ante Morbi eget arcu Morbi porta libero id ullamcorper nonummy nibh ligula pulvinar metus eget consv et scelerisque mi tortor at ipsum</p>
</section>

<section class="segment seg-res abs">
  <h2>Residential</h2>
  <h3>Morbi diam mauris viverra</h3>
  <p>gravida eu mattis in ante Morbi eget arcu Morbi porta libero id ullamcorper nonummy nibh ligula pulvinar metus eget consv et scelerisque mi</p>
</section>
<section class="segment seg-com abs">
  <h2>Commerical</h2>
  <h3>Morbi diam mauris viverra</h3>
  <p>gravida eu mattis in ante Morbi eget arcu Morbi porta libero id ullamcorper nonummy nibh ligula pulvinar metus eget consv</p>
</section>

<section class="why">
  <h2 class="abs">Why Choose Our Product</h2>
  <div class="why-photo abs" role="img" aria-label="Close-up of burning logs"></div>
  <p class="abs">Etiam eu urna Sed porta Suspendisse quam leo molestie sed luctus quis feugiat in pede Fusce tellus Sed metus augue convallis et vehicula ut pulvinar eu ante Integer orci tellus tristique vitae consequat nec porta vel lectus Nulla sit amet diam Duis non nunclibero a tempus libero lectus feugiat felis Morbi diam mauris viverra in gravida eu mattis in ante Morbi eget arcu</p>
</section>

<aside class="order-box abs">
  <div class="order-head">Online Order Now</div>
  <div class="order-photo" role="img" aria-label="Customer service operator taking a phone order"></div>
  <div class="order-title">Morbi porta libero id ullamcorper</div>
  <div class="order-text">Nonummy, nibh ligula pulvinar metus, eget consectetuer augue nisi quis lacus.</div>
  <div class="order-btn">ORDER NOW</div>
</aside>

<aside class="offers">
  <h2 class="abs">Special Offers</h2>
  <h3 class="abs">Nunc porta convallis pede</h3>
  <p class="abs p1">Phasellus felis dolor, scelerisque a, tempus eget, lobortis id, libero. Donec scelerisque leo ac risus. Praesent sit amet est. In dictum, dolor eu dictum porttitor, enim felis viverra mi, eget luctus massa purus quis odio.</p>
  <p class="abs p2">Etiam nulla massa, pharetra facilisis,</p>
</aside>

<footer class="site-footer abs">
  <div class="foot-links abs">Home<span>|</span>ABOUT US<span>|</span>FIRE WQOD<span>|</span>PRICE<span>|</span>DELIVERY<span>|</span>ACCESORIES<span>|</span>ORDER NOW<span>|</span>SUPPORT<span>|</span>CONTACT</div>
  <div class="copyright abs">© 2013 Company Name.&nbsp; All right reserved.&nbsp; Term of Use</div>
  <div class="social abs" aria-label="Social links">
    <span style="background:#3b5a9a"></span>
    <span style="background:#33aee0"></span>
    <span style="background:#1d7fb8"></span>
    <span style="background:#f08a1c"></span>
  </div>
  <div class="cards abs" aria-label="Accepted payment cards">
    <span></span><span></span><span></span><span></span>
  </div>
</footer>

</body>
</html>
```